Vorapo Business Card

Need a double sided business card. Would like the business card to have the logo on one side and the employees details and business contact details on the other.

Business

```html
<!DOCTYPE html>
<html lang="en">
<head>
<meta charset="utf-8">
<title>Vorapo Business Card</title>
<link rel="stylesheet" href="https://fonts.googleapis.com/css2?family=Lato:wght@300;400;700;900&display=swap">
<style>
  :root {
    --bg: #e4e5e7;
    --green-light: #a3d03f;
    --green-dark: #69bb45;
    --green-text: #6fa52f;
    --ink: #1a1a1a;
    --band: #0d0d0d;
    --white: #ffffff;
    --icon-gray: #8a8f94;
  }
  * { box-sizing: border-box; margin: 0; padding: 0; }
  html, body {
    width: 1200px; height: 926px; overflow: hidden;
    background: var(--bg);
    font-family: "Lato", Arial, sans-serif;
  }
  .sheet {
    position: relative; width: 1200px; height: 926px;
    display: flex; flex-direction: column; align-items: center;
    justify-content: center; gap: 56px;
  }
  .card {
    position: relative; width: 660px; height: 377px;
    overflow: hidden; box-shadow: 0 6px 18px rgba(0,0,0,0.18);
  }

  /* Front side */
  .card-front {
    background: linear-gradient(160deg, var(--green-light) 0%, var(--green-dark) 100%);
  }
  .front-logo {
    position: absolute; left: 0; right: 0; top: 118px;
    display: flex; justify-content: center; align-items: center; gap: 12px;
    color: var(--white); font-weight: 900; font-size: 64px; letter-spacing: 1px;
  }
  .logo-square { width: 22px; height: 22px; background: currentColor; }
  .address-band {
    position: absolute; left: 0; right: 0; bottom: 0; height: 66px;
    background: var(--band); color: var(--white);
    display: flex; align-items: center; gap: 12px; padding-left: 26px;
    font-size: 17px; font-weight: 400; white-space: nowrap;
  }
  .address-band svg { width: 20px; height: 20px; flex: none; }

  /* Back side */
  .card-back { background: var(--white); }
  .back-logo {
    position: absolute; left: 34px; top: 30px;
    display: flex; align-items: center; gap: 8px;
    color: var(--green-light); font-weight: 900; font-size: 40px;
  }
  .back-logo .logo-square { width: 14px; height: 14px; }
  .person {
    position: absolute; right: 40px; top: 90px; text-align: right;
  }
  .person-name {
    font-size: 31px; color: var(--ink); font-weight: 400; letter-spacing: 0.5px;
  }
  .person-name strong { font-weight: 900; }
  .person-role {
    font-size: 17px; font-weight: 700; color: var(--green-text); letter-spacing: 1px; margin-top: 2px;
  }
  .contact-list {
    position: absolute; list-style: none;
    display: flex; flex-direction: column; gap: 10px;
    font-size: 19px; color: var(--ink);
  }
  .contact-list li { display: flex; align-items: center; gap: 12px; }
  .contact-phones { left: 34px; bottom: 70px; }
  .contact-web { right: 40px; bottom: 40px; }
  .icon-box {
    width: 22px; height: 22px; border-radius: 4px; background: var(--ink);
    display: flex; align-items: center; justify-content: center; flex: none;
  }
  .icon-box svg { width: 14px; height: 14px; }
</style>
</head>
<body>
<main class="sheet">

  <section class="card card-front" aria-label="Card front">
    <div class="front-logo"><span>vorapo</span><span class="logo-square"></span></div>
    <div class="address-band">
      <svg viewBox="0 0 20 20" aria-hidden="true"><path d="M10 2 1 10h3v8h5v-5h2v5h5v-8h3z" fill="#fff"/></svg>
      <span>27 Larch Lane, Brookfield, BF4 7QN, 27 Larch Lane, Brookfield, BF4 7QN</span>
    </div>
  </section>

  <section class="card card-back" aria-label="Card back">
    <div class="back-logo"><span>vorapo</span><span class="logo-square"></span></div>

    <div class="person">
      <p class="person-name">MARK <strong>ELLISON</strong></p>
      <p class="person-role">OWNER/C.E.O</p>
    </div>

    <ul class="contact-list contact-phones">
      <li>
        <span class="icon-box"><svg viewBox="0 0 14 14" aria-hidden="true"><path d="M2 4c0-1 1-2 5-2s5 1 5 2v1H9V4H5v1H2zM3 6h8l1 6H2z" fill="#fff"/></svg></span>
        <span>+ 123 - 4820 - 5517</span>
      </li>
      <li>
        <span class="icon-box"><svg viewBox="0 0 14 14" aria-hidden="true"><rect x="4" y="1" width="6" height="12" rx="1" fill="#fff"/><rect x="5" y="3" width="4" height="7" fill="#1a1a1a"/></svg></span>
        <span>+ 987 - 3160 - 4428</span>
      </li>
    </ul>

    <ul class="contact-list contact-web">
      <li>
        <span class="icon-box"><svg viewBox="0 0 14 14" aria-hidden="true"><rect x="1.5" y="3" width="11" height="8" fill="none" stroke="#fff" stroke-width="1.4"/><path d="M1.5 3 7 8l5.5-5" fill="none" stroke="#fff" stroke-width="1.4"/></svg></span>
        <span>hello@vorapomail.com</span>
      </li>
      <li>
        <span class="icon-box"><svg viewBox="0 0 14 14" aria-hidden="true"><path d="M6 8 8 6M5 6.5 3.5 8a2 2 0 0 0 2.8 2.8L7.8 9.3M9 7.5 10.5 6A2 2 0 0 0 7.7 3.2L6.2 4.7" fill="none" stroke="#fff" stroke-width="1.5" stroke-linecap="round"/></svg></span>
        <span>www.vorapoweb.com</span>
      </li>
    </ul>
  </section>

</main>
</body>
</html>
```